Modern Web Design for Nonprofit Organization

Our client is looking to redesign their website. They want a modern look, clean and professional, that integrates their new brand guidelines.

Here is clients current site:
http://www.valorandes.org/

They want their own unique design but here are some sites the clients likes:
https://www.brixtonvane.com/en/
https://oakhollowrise.org/
https://www.lumacraft.com/
https://www.tbnlawgroup.com/
https://www.greyharborco.org/

Attached please find the clients logos, color palette, site plan and design specs.

You will create a homepage mockup that will have the following sections in this order:
1. Thin Alert Bar at very top with one line message
2. Nav Bar with Logo and Main Nav (red in site plan)
3. Hero Image or Video
4. Signup Bar with name email and zip and connect button
5. Intro section with image, welcome message, and supporter counter
6. Featured Action section with call to action
7. Event section with two upcoming event cards
8. Latest News section with three latest blog post
9. Support our work (donation) section
10. Worker and Member Stories Section with feed of social posts
11. Footer.

You can use text and images from clients existing site or placeholder images and placeholder text.

Please submit as many home page mockups/idea boards as you like. Client will pick the top three and ask for some revisions. If you are selected this will lead to a lot of work for this client.

Project is private please adhere to ArtPlenary terms of use and do not share any materials please.

QUICKEST RESPONSE PLEASE!

Thanks for looking!

Target Market(s)

Non profit donors and farmworker advocates

Number of Pages Required

2 page

Font styles to use
Sans Serif

Requirements
Must have
• Adhere to brief and client brand ID
Nice to have
• World class design

```html
<!DOCTYPE html>
<html lang="en">
<head>
<meta charset="utf-8">
<title>Campo Roots Foundation — Home</title>
<link href="https://fonts.googleapis.com/css2?family=Fira+Sans+Condensed:wght@400;500;600;700&display=swap" rel="stylesheet">
<style>
:root{
  --red:#d40b0b;
  --teal:#0b8e96;
  --yellow:#ffc400;
  --mist:#bcc9c9;
  --ink:#161616;
  --body:#333;
  --line:#e2e2e2;
  --blue:#2d5ba8;
  --sky:#2f9be0;
}
*{box-sizing:border-box;margin:0;padding:0}
html,body{width:1200px;height:3076px;overflow:hidden}
body{font-family:"Fira Sans Condensed",sans-serif;color:var(--ink);background:#fff;position:relative}
.abs{position:absolute}
.alert-bar{top:0;left:0;width:1200px;height:30px;background:var(--red);color:#fff;font-size:10px;font-weight:600;letter-spacing:1.2px;text-align:center;line-height:30px}
.nav{top:30px;left:0;width:1200px;height:75px;display:flex;align-items:center;padding:0 158px}
.brand{display:flex;align-items:center;gap:8px;font-weight:700;font-size:11px;line-height:1.05;width:220px}
.brand-dot{width:26px;height:26px;border-radius:50%;background:var(--red)}
.menu{display:flex;gap:0;list-style:none;flex:1;justify-content:space-between;padding-left:10px;padding-right:40px;font-size:10px;font-weight:500}
.menu li{display:flex;align-items:center;gap:4px}
.menu li.active{color:var(--red)}
.menu svg{width:8px;height:8px}
.btn{display:inline-block;border-radius:7px;font-weight:600;text-align:center}
.btn-donate{background:var(--yellow);color:var(--ink);font-size:10px;width:75px;height:30px;line-height:30px}
.hero{top:105px;left:0;width:1200px;height:600px;background:linear-gradient(160deg,#5d6a3e 0%,#3d5a2a 35%,#6b5b4a 55%,#2f5422 80%,#3f6a2a 100%)}
.signup{top:705px;left:0;width:1200px;height:75px;background:var(--mist);display:flex;align-items:center;font-weight:500;font-size:15px}
.signup-label{position:absolute;left:215px}
.signup-form{position:absolute;left:388px;width:300px;height:30px;background:#fff;border-radius:6px;display:flex;align-items:center;font-size:9px;color:#444;padding-left:15px}
.signup-form .btn{position:absolute;right:0;top:0;height:30px;width:75px;line-height:30px;background:var(--teal);color:#fff;font-size:9px;border-radius:6px}
.connect{position:absolute;left:725px}
.social{display:flex;gap:9px}
.social span{width:29px;height:29px;border-radius:50%}
.social .s1{background:var(--blue)}
.social .s2{background:var(--sky)}
.signup .social{position:absolute;left:915px}
.intro-photo{top:840px;left:158px;width:434px;height:442px;background:radial-gradient(circle at 50% 45%,#c8a36b 0%,#6d8a2e 45%,#2d4d16 100%)}
.welcome{top:895px;left:666px;width:376px}
.welcome h1{font-size:45px;font-weight:700;margin-bottom:22px}
.welcome p{font-size:11px;line-height:22.5px;color:var(--body)}
.stats{top:1155px;left:666px;width:376px;height:62px;display:flex;justify-content:space-between}
.stat{text-align:center;font-size:18px;font-weight:600;line-height:1.2}
.stat small{display:block;color:var(--red);font-size:14px;font-weight:500}
.stat-sep{width:1px;background:#333;height:60px}
.section-title{left:0;width:1200px;text-align:center;font-size:21px;font-weight:700}
.actions{top:1428px;left:140px;width:920px;display:flex}
.action{width:184px;text-align:center;display:flex;flex-direction:column;align-items:center}
.action svg{width:80px;height:80px;stroke:var(--red);fill:none;stroke-width:2.5;stroke-linecap:round;stroke-linejoin:round}
.action h3{font-size:18px;font-weight:600;height:56px;display:flex;align-items:center;line-height:1.25;margin-top:8px}
.action p{font-size:11px;line-height:18px;color:var(--body);width:130px;margin-top:8px;height:80px}
.btn-teal{background:var(--teal);color:#fff;font-size:9px;width:75px;height:28px;line-height:28px;margin-top:20px}
.event{top:1832px;width:434px;height:112px;border:1px solid var(--line);display:flex}
.event-date{width:112px;height:112px;background:var(--red);color:#fff;text-align:center;padding-top:14px}
.event-date b{display:block;font-size:58px;font-weight:400;line-height:1}
.event-date small{font-size:11px;font-weight:600;letter-spacing:.5px}
.event-body{padding:18px 14px;font-size:11px;color:var(--body);line-height:1.3}
.event-body h4{font-size:14px;font-weight:600;color:var(--ink);margin-bottom:2px}
.attend{display:flex;align-items:center;gap:6px;margin-top:12px;font-size:9px}
.attend svg{width:14px;height:14px;stroke:#333;fill:none;stroke-width:1.5}
.news{top:2060px;width:285px;height:187px}
.news-photo{background:radial-gradient(circle at 50% 50%,#c8a36b 0%,#6d8a2e 45%,#2d4d16 100%)}
.news-feature{background:linear-gradient(135deg,#c8190f,#e23319 60%,#b0150c);color:#fff;padding:48px 37px}
.news-feature h4{font-size:18px;font-weight:700;line-height:1.25}
.news-feature a{display:block;margin-top:8px;color:#fff;font-size:9px;font-weight:600;text-decoration:underline}
.support{top:2307px;left:0;width:1200px;height:145px;background:linear-gradient(90deg,#3a3c2c,#4a5a30 40%,#3e4a2c 70%,#343628);color:#fff;text-align:center;padding-top:38px}
.support h2{font-size:21px;font-weight:700;margin-bottom:10px}
.support .btn{width:75px;height:28px;line-height:28px;font-size:9px;background:var(--yellow);color:var(--ink)}
.stories{top:2510px;left:158px;width:380px}
.stories h2{font-size:21px;font-weight:700}
.quote-mark{font-size:40px;font-weight:700;line-height:1;margin-top:14px;height:26px}
.stories p{font-size:11px;line-height:22.5px;color:var(--body);padding-left:24px;margin-top:0}
.stories cite{display:block;text-align:right;font-style:normal;font-size:17px;font-weight:600;margin-top:20px}
.arrows{display:flex;gap:15px;margin-top:40px}
.arrows span{width:22px;height:22px;border-radius:50%;background:var(--teal);display:flex;align-items:center;justify-content:center}
.arrows svg{width:10px;height:10px;stroke:#fff;fill:none;stroke-width:2}
.feed{top:2512px;left:607px;width:435px;height:435px;display:grid;grid-template-columns:repeat(4,1fr);grid-template-rows:repeat(4,1fr);gap:4px}
.feed div{border-radius:0}
.f-boots{background:linear-gradient(180deg,#4b6088,#8e8a82 70%,#b5ab9c)}
.f-field{background:linear-gradient(180deg,#6ea4e0 0%,#b6d2ef 40%,#2f7c34 55%,#3b6a2c)}
.f-crop{background:linear-gradient(180deg,#c5c9a8,#4e7f2e 50%,#2d4d1b)}
.f-worker{background:radial-gradient(circle,#c8a36b,#5f8a2a 55%,#2d4d16)}
.f-pick{background:linear-gradient(160deg,#5a7a3a,#3e6a28 50%,#7a6a55)}
.big1{grid-column:1/3;grid-row:1/3}
.big2{grid-column:3/5;grid-row:3/5}
.footer{top:3008px;left:0;width:1200px;height:68px;background:var(--mist);display:flex;align-items:center;justify-content:center;gap:0;font-size:11px;font-weight:500}
.footer ul{list-style:none;display:flex;gap:0}
.footer li{margin:0 26px}
.footer .social{margin-left:8px}
.footer .social span{width:22px;height:22px}
</style>
</head>
<body>

<div class="abs alert-bar">COVID-19 NOTICE - WEAR MASK ANYWHERE YOU GO</div>

<header class="abs nav">
  <div class="brand"><span class="brand-dot"></span><span>CAMPO ROOTS<br>FOUNDATION</span></div>
  <ul class="menu">
    <li class="active">HOME</li>
    <li>GET HELP NOW <svg viewBox="0 0 10 10"><path d="M1 3l4 4 4-4" stroke="#222" fill="none" stroke-width="1.3"/></svg></li>
    <li>TAKE ACTION <svg viewBox="0 0 10 10"><path d="M1 3l4 4 4-4" stroke="#222" fill="none" stroke-width="1.3"/></svg></li>
    <li>NEWS AND EVENTS <svg viewBox="0 0 10 10"><path d="M1 3l4 4 4-4" stroke="#222" fill="none" stroke-width="1.3"/></svg></li>
    <li>SUPPORT OUR WORK <svg viewBox="0 0 10 10"><path d="M1 3l4 4 4-4" stroke="#222" fill="none" stroke-width="1.3"/></svg></li>
    <li>ABOUT US</li>
  </ul>
  <span class="btn btn-donate">DONATE</span>
</header>

<div class="abs hero" role="img" aria-label="Farmworkers in straw hats harvesting leafy greens in a field"></div>

<section class="abs signup">
  <span class="signup-label">Sign Up &amp; Stay Informed</span>
  <div class="signup-form">Type your email here<span class="btn">SUBMIT</span></div>
  <span class="connect">Or connect with us through</span>
  <div class="social"><span class="s1"></span><span class="s2"></span></div>
</section>

<div class="abs intro-photo" role="img" aria-label="Smiling farmworker holding a crate of freshly harvested cacao pods"></div>
<section class="abs welcome">
  <h1>Welcome!</h1>
  <p>The Campo Roots Foundation is a dynamic nonprofit organization established in 2006. The Campo Roots Foundation’s core purpose is to empower communities to ensure human dignity. We serve over 90,000 immigrants annually through a holistic approach; we provide critical services and engage our constituents in systemic change to break the cycle of poverty. Our regional offices are safe havens that provide resources and services—such as credible immigration legal advice—and act as hubs for educational outreach and organizing.</p>
</section>
<div class="abs stats">
  <div class="stat">10, 000<small>SUPPORTERS</small></div>
  <div class="stat-sep"></div>
  <div class="stat">5, 000<small>VOLUNTEERS</small></div>
  <div class="stat-sep"></div>
  <div class="stat">$15, 000<small>DONATIONS</small></div>
</div>

<h2 class="abs section-title" style="top:1338px">FEATURED ACTIONS</h2>
<section class="abs actions">
  <div class="action">
    <svg viewBox="0 0 80 80"><path d="M26 22h28M30 22v-8h20v8"/><path d="M31 24v8a9 9 0 0 0 18 0v-8"/><path d="M20 70v-16a10 10 0 0 1 10-10h20a10 10 0 0 1 10 10v16z"/><path d="M32 44v26M48 44v26M32 56h16"/></svg>
    <h3>Farmworker<br>Legalization</h3>
    <p>Action page detailing a key advocacy item. Users can learn more and sign to add their name in support.</p>
    <span class="btn btn-teal">READ MORE</span>
  </div>
  <div class="action">
    <svg viewBox="0 0 80 80"><circle cx="40" cy="40" r="15"/><path d="M40 12v8M40 60v8M12 40h8M60 40h8M20 20l6 6M54 54l6 6M60 20l-6 6M26 54l-6 6"/></svg>
    <h3>Heat</h3>
    <p>Action page detailing a key advocacy item. Users can learn more and sign to add their name in support.</p>
    <span class="btn btn-teal">READ MORE</span>
  </div>
  <div class="action">
    <svg viewBox="0 0 80 80"><path d="M32 30h16v8l6 8v24H26V46l6-8z"/><path d="M34 30v-10h12v10M46 22h14M54 18v8"/><circle cx="40" cy="56" r="8"/><path d="M34 50l12 12"/></svg>
    <h3>Pesticides</h3>
    <p>Action page detailing a key advocacy item. Users can learn more and sign to add their name in support.</p>
    <span class="btn btn-teal">READ MORE</span>
  </div>
  <div class="action">
    <svg viewBox="0 0 80 80"><path d="M24 52a10 10 0 0 1-4-19 12 12 0 0 1 18-12 12 12 0 0 1 20 6 10 10 0 0 1 2 19 8 8 0 0 1-12 6z"/><circle cx="24" cy="62" r="3"/><circle cx="18" cy="70" r="2"/></svg>
    <h3>Dream Act</h3>
    <p>Action page detailing a key advocacy item. Users can learn more and sign to add their name in support.</p>
    <span class="btn btn-teal">READ MORE</span>
  </div>
  <div class="action">
    <svg viewBox="0 0 80 80"><path d="M20 18l10-6 10 16-10 6z"/><path d="M35 31l10 14h8a6 6 0 0 1 6 6v6l-8 10H44L34 52"/><path d="M48 20l6 4M56 30l6 2"/></svg>
    <h3>Worker Rights</h3>
    <p>Action page detailing a key advocacy item. Users can learn more and sign to add their name in support.</p>
    <span class="btn btn-teal">READ MORE</span>
  </div>
</section>

<h2 class="abs section-title" style="top:1773px;left:-13px">UPCOMING EVENTS</h2>
<article class="abs event" style="left:158px">
  <div class="event-date"><b>30</b><small>OCT 2020</small></div>
  <div class="event-body">
    <h4>ESSECNTIAL FARM WORK RPOJECT</h4>
    Lorem ipsum dolor sit amet, consectetur adipiscing elit, sed do eiusmod tempor incididunt ut labore et dolore magna aliqua.
    <div class="attend"><svg viewBox="0 0 14 14"><circle cx="7" cy="4" r="3"/><path d="M1 13a6 6 0 0 1 12 0z"/></svg><span><b>5, 000</b> Attending</span></div>
  </div>
</article>
<article class="abs event" style="left:608px">
  <div class="event-date"><b>01</b><small>NOV 2020</small></div>
  <div class="event-body">
    <h4>ESSECNTIAL FARM WORK RPOJECT</h4>
    Lorem ipsum dolor sit amet, consectetur adipiscing elit, sed do eiusmod tempor incididunt ut labore et dolore magna aliqua.
    <div class="attend"><svg viewBox="0 0 14 14"><circle cx="7" cy="4" r="3"/><path d="M1 13a6 6 0 0 1 12 0z"/></svg><span><b>5, 000</b> Attending</span></div>
  </div>
</article>

<h2 class="abs section-title" style="top:2001px">LATEST NEWS</h2>
<div class="abs news news-photo" style="left:158px" role="img" aria-label="Farmworker holding a crate of harvested produce"></div>
<article class="abs news news-feature" style="left:457px">
  <h4>In Kansas and Missouri, Immigrants are Rooted in the Agriculture Workforce</h4>
  <a>Read more &gt;</a>
</article>
<div class="abs news news-photo" style="left:757px" role="img" aria-label="Farmworker holding a crate of harvested produce"></div>

<section class="abs support" role="img" aria-label="Dark-toned band over a photo of leafy crops">
  <h2>SUPPORT OUR WORK</h2>
  <span class="btn">DONATE</span>
</section>

<section class="abs stories">
  <h2>WORKERS AND MEMEBERS’ STORIES</h2>
  <div class="quote-mark">“</div>
  <p>Lorem ipsum dolor sit amet, consectetur adipiscing elit, sed do eiusmod tempor incididunt ut labore et dolore magna aliqua. Quis ipsum suspendisse ultrices gravida. Risus commodo viverra maecenas accumsan lacus vel facilisis. Lorem ipsum dolor sit amet, consectetur adipiscing elit, sed do eiusmod tempor incididunt ut labore et dolore magna aliqua. Quis ipsum suspendisse ultrices gravida. Risus commodo viverra maecenas accumsan lacus vel facilisis. Lorem ipsum dolor sit amet, consectetur adipiscing elit, sed do eiusmod tempor incididunt ut labore et dolore magna aliqua. Quis ipsum suspendisse ultrices gravida. Risus commodo viverra maecenas accumsan lacus vel facilisis.</p>
  <cite>- John Doe</cite>
  <div class="arrows">
    <span><svg viewBox="0 0 10 10"><path d="M6.5 2L3.5 5l3 3"/></svg></span>
    <span><svg viewBox="0 0 10 10"><path d="M3.5 2l3 3-3 3"/></svg></span>
  </div>
</section>

<div class="abs feed">
  <div class="f-boots big1" role="img" aria-label="Workers' boots standing on a dirt path"></div>
  <div class="f-field" role="img" aria-label="Green crop rows under a blue sky"></div>
  <div class="f-crop" role="img" aria-label="Rows of leafy crops"></div>
  <div class="f-worker" role="img" aria-label="Farmworker holding harvested produce"></div>
  <div class="f-pick" role="img" aria-label="Farmworker picking greens"></div>
  <div class="f-field" role="img" aria-label="Green crop rows under a blue sky"></div>
  <div class="f-crop" role="img" aria-label="Rows of leafy crops"></div>
  <div class="f-boots big2" role="img" aria-label="Workers' boots standing on a dirt path"></div>
  <div class="f-worker" role="img" aria-label="Farmworker holding harvested produce"></div>
  <div class="f-pick" role="img" aria-label="Farmworker picking greens"></div>
</div>

<footer class="abs footer">
  <ul>
    <li>Join</li><li>Private Policy</li><li>Terms of Services</li><li>Careers</li><li>Contact Us</li><li>Donate Now</li><li>Find us on Social</li>
  </ul>
  <div class="social"><span class="s1"></span><span class="s2"></span></div>
</footer>

</body>
</html>
```